Pebble Ledger WEB application

We need a small webdesign for a WEB-Application. Functionality will be provided by our developers. All we need are templates with HTML5, CSS and Java functionality for the "animated" parts. As well as some images and logos .
See attached Powerpoint. Please ignore last slide.
Design should be state of the art material design as know from Quorvix or Zelpad latest OS versions
In the end will be fluid design (fitting automatically to actual screen size) but template should base on 540 x 960

Target Market(s)

UK Mobile Market

Number of Pages Required

5+ page

Font styles to use
Sans Serif

Requirements
Must have
• next to requierements in Powerpoint we need animations as stated in PP (progress animation).
Nice to have
• All textfiles should be in a XML file to be easily translated to other languages.Can be done by our developers as well

```html
<!DOCTYPE html>
<html lang="en">
<head>
<meta charset="utf-8">
<title>Pebble Ledger – Scanning</title>
<link rel="stylesheet" href="https://fonts.googleapis.com/css2?family=Open+Sans:wght@400;600&display=swap">
<style>
:root{
  --green:#5bbd3c;
  --green-light:#7fd05a;
  --green-dark:#3f9a26;
  --ink:#2f2f2f;
  --label:#555;
  --panel:#eeeeee;
  --rule:#d9d9d9;
  --track:#e2e2e2;
  --idle:#c9c9c9;
  --bar-dark:#0f0f0f;
  --bar-mid:#3a3a3a;
  --white:#fff;
}
*{box-sizing:border-box;margin:0;padding:0}
html,body{width:675px;height:1200px;overflow:hidden;background:var(--white)}
body{font-family:"Open Sans",Arial,sans-serif;position:relative}

.status-bar{position:absolute;top:0;left:0;width:675px;height:40px;background:var(--white);
  display:flex;align-items:center;justify-content:space-between;padding:0 16px;font-size:22px;color:#111;font-weight:600}
.status-left{display:flex;align-items:center;gap:8px}
.status-right{display:flex;align-items:center;gap:6px}

.app-header{position:absolute;top:40px;left:0;width:675px;height:136px;
  background:linear-gradient(#3a3a3a,#0c0c0c);display:flex;align-items:center;justify-content:center}
.app-title{color:var(--white);font-size:46px;font-weight:400;letter-spacing:.5px}

.scan-panel{position:absolute;top:176px;left:0;width:675px;height:911px;background:var(--panel)}
.scan-heading{position:absolute;top:46px;width:100%;text-align:center;font-size:36px;color:var(--ink);letter-spacing:1px}
.scan-subheading{position:absolute;top:96px;width:100%;text-align:center;font-size:33px;color:var(--green)}

.check-list{position:absolute;top:184px;left:0;width:675px;list-style:none;border-top:2px solid var(--rule)}
.check-row{height:77px;border-bottom:2px solid var(--rule);display:flex;align-items:center;position:relative}
.check-row:last-child{border-bottom:none}
.row-icon{width:40px;height:40px;margin-left:22px}
.row-label{margin-left:20px;font-size:22px;color:var(--label);width:195px}
.progress-track{position:absolute;left:277px;width:274px;height:12px;border-radius:6px;background:var(--track);
  box-shadow:inset 0 1px 2px rgba(0,0,0,.15);overflow:hidden}
.progress-fill{height:100%;border-radius:6px;background:linear-gradient(var(--green-light),var(--green-dark))}
.row-state{position:absolute;left:614px;width:38px;height:38px}

.results-button{position:absolute;top:769px;left:142px;width:391px;height:92px;border-radius:4px;
  background:linear-gradient(var(--green-light),var(--green-dark));color:var(--white);font-size:34px;
  display:flex;align-items:center;justify-content:center;box-shadow:0 3px 4px rgba(0,0,0,.25)}

.tab-bar{position:absolute;top:1087px;left:0;width:675px;height:113px;background:linear-gradient(#2b2b2b,#080808);display:flex}
.tab{flex:1;display:flex;flex-direction:column;align-items:center;justify-content:flex-end;padding-bottom:12px;
  color:var(--white);font-size:20px;border-right:2px solid #000;box-shadow:inset -1px 0 0 #444}
.tab:last-child{border-right:none;box-shadow:none}
.tab svg{width:46px;height:46px;margin-bottom:14px}
</style>
</head>
<body>

<div class="status-bar">
  <div class="status-left">
    <svg width="86" height="16" viewBox="0 0 86 16"><g fill="#111"><circle cx="8" cy="8" r="7"/><circle cx="25" cy="8" r="7"/><circle cx="42" cy="8" r="7"/></g><g fill="none" stroke="#111" stroke-width="1.5"><circle cx="59" cy="8" r="6"/><circle cx="76" cy="8" r="6"/></g></svg>
    <svg width="28" height="20" viewBox="0 0 28 20"><g fill="none" stroke="#111" stroke-width="3" stroke-linecap="round"><path d="M2 7a17 17 0 0 1 24 0"/><path d="M7 12a10 10 0 0 1 14 0"/></g><circle cx="14" cy="17" r="2.5" fill="#111"/></svg>
  </div>
  <span>4:39 PM</span>
  <div class="status-right">
    <span>100%</span>
    <svg width="50" height="22" viewBox="0 0 50 22"><rect x="1" y="1" width="43" height="20" rx="3" fill="none" stroke="#111" stroke-width="2"/><rect x="4" y="4" width="37" height="14" fill="#111"/><rect x="45" y="7" width="4" height="8" fill="#111"/></svg>
  </div>
</div>

<header class="app-header"><h1 class="app-title">Pebble Ledger</h1></header>

<main class="scan-panel">
  <h2 class="scan-heading">SCANNING</h2>
  <p class="scan-subheading">Analyzing in progress...</p>

  <ul class="check-list">
    <li class="check-row">
      <svg class="row-icon" viewBox="0 0 40 40"><g fill="var(--green)"><path d="M17 3h6l1 5 4 2 4-3 4 4-3 4 2 4 5 1v6l-5 1-2 4 3 4-4 4-4-3-4 2-1 5h-6l-1-5-4-2-4 3-4-4 3-4-2-4-5-1v-6l5-1 2-4-3-4 4-4 4 3 4-2z"/></g><circle cx="20" cy="20" r="6" fill="var(--panel)"/></svg>
      <span class="row-label">System</span>
      <div class="progress-track"><div class="progress-fill" style="width:100%"></div></div>
      <svg class="row-state" viewBox="0 0 38 38"><path d="M4 20l10 10L34 6" fill="none" stroke="var(--green)" stroke-width="6" stroke-linecap="round" stroke-linejoin="round"/></svg>
    </li>
    <li class="check-row">
      <svg class="row-icon" viewBox="0 0 40 40"><path d="M6 10h14l4-4h10v28H6z" fill="var(--green)"/><g fill="var(--panel)"><rect x="10" y="13" width="3" height="7"/><rect x="15" y="13" width="3" height="7"/><rect x="20" y="11" width="3" height="9"/><rect x="25" y="9" width="3" height="11"/></g></svg>
      <span class="row-label">Memory</span>
      <div class="progress-track"><div class="progress-fill" style="width:64%"></div></div>
      <svg class="row-state" viewBox="0 0 38 38"><g fill="none" stroke="var(--green)" stroke-width="4"><path d="M8 22a11 11 0 0 1 19-13"/><path d="M30 16a11 11 0 0 1-19 13"/></g><path d="M23 4l8 1-1 8z M15 34l-8-1 1-8z" fill="var(--green)"/></svg>
    </li>
    <li class="check-row">
      <svg class="row-icon" viewBox="0 0 40 40"><rect x="4" y="6" width="32" height="28" fill="none" stroke="var(--green)" stroke-width="3"/><rect x="4" y="6" width="32" height="7" fill="var(--green)"/><g fill="var(--green)"><rect x="9" y="17" width="6" height="4"/><rect x="17" y="17" width="6" height="4"/><rect x="25" y="17" width="6" height="4"/><rect x="9" y="25" width="6" height="4"/><rect x="17" y="25" width="6" height="4"/><rect x="25" y="25" width="6" height="4"/></g></svg>
      <span class="row-label">Accounts</span>
      <div class="progress-track"></div>
      <svg class="row-state" viewBox="0 0 38 38"><g fill="none" stroke="var(--idle)" stroke-width="4"><path d="M8 22a11 11 0 0 1 19-13"/><path d="M30 16a11 11 0 0 1-19 13"/></g><path d="M23 4l8 1-1 8z M15 34l-8-1 1-8z" fill="var(--idle)"/></svg>
    </li>
    <li class="check-row">
      <svg class="row-icon" viewBox="0 0 38 38"><g fill="none" stroke="var(--green)" stroke-width="4"><path d="M8 22a11 11 0 0 1 19-13"/><path d="M30 16a11 11 0 0 1-19 13"/></g><path d="M23 4l8 1-1 8z M15 34l-8-1 1-8z" fill="var(--green)"/></svg>
      <span class="row-label">Sync Processes</span>
      <div class="progress-track"></div>
      <svg class="row-state" viewBox="0 0 38 38"><g fill="none" stroke="var(--idle)" stroke-width="4"><path d="M8 22a11 11 0 0 1 19-13"/><path d="M30 16a11 11 0 0 1-19 13"/></g><path d="M23 4l8 1-1 8z M15 34l-8-1 1-8z" fill="var(--idle)"/></svg>
    </li>
    <li class="check-row">
      <svg class="row-icon" viewBox="0 0 40 40"><path d="M20 3a12 12 0 0 1 12 12c0 9-12 22-12 22S8 24 8 15A12 12 0 0 1 20 3z" fill="var(--green)"/><circle cx="20" cy="15" r="5" fill="var(--panel)"/></svg>
      <span class="row-label">Localization</span>
      <div class="progress-track"></div>
      <svg class="row-state" viewBox="0 0 38 38"><g fill="none" stroke="var(--idle)" stroke-width="4"><path d="M8 22a11 11 0 0 1 19-13"/><path d="M30 16a11 11 0 0 1-19 13"/></g><path d="M23 4l8 1-1 8z M15 34l-8-1 1-8z" fill="var(--idle)"/></svg>
    </li>
    <li class="check-row">
      <svg class="row-icon" viewBox="0 0 40 40"><circle cx="12" cy="20" r="4" fill="var(--green)"/><g fill="none" stroke="var(--green)" stroke-width="3" stroke-linecap="round"><path d="M19 12a11 11 0 0 1 0 16"/><path d="M25 7a18 18 0 0 1 0 26"/></g></svg>
      <span class="row-label">Linkwave</span>
      <div class="progress-track"></div>
      <svg class="row-state" viewBox="0 0 38 38"><g fill="none" stroke="var(--idle)" stroke-width="4"><path d="M8 22a11 11 0 0 1 19-13"/><path d="M30 16a11 11 0 0 1-19 13"/></g><path d="M23 4l8 1-1 8z M15 34l-8-1 1-8z" fill="var(--idle)"/></svg>
    </li>
    <li class="check-row">
      <svg class="row-icon" viewBox="0 0 40 40"><rect x="9" y="3" width="22" height="34" rx="3" fill="none" stroke="var(--green)" stroke-width="3"/><g fill="var(--green)"><rect x="13" y="9" width="6" height="6"/><rect x="21" y="9" width="6" height="6"/><rect x="13" y="18" width="6" height="6"/><rect x="21" y="18" width="6" height="6"/></g></svg>
      <span class="row-label">Apps</span>
      <div class="progress-track"></div>
      <svg class="row-state" viewBox="0 0 38 38"><g fill="none" stroke="var(--idle)" stroke-width="4"><path d="M8 22a11 11 0 0 1 19-13"/><path d="M30 16a11 11 0 0 1-19 13"/></g><path d="M23 4l8 1-1 8z M15 34l-8-1 1-8z" fill="var(--idle)"/></svg>
    </li>
  </ul>

  <div class="results-button">Show Results</div>
</main>

<nav class="tab-bar">
  <div class="tab">
    <svg viewBox="0 0 38 38"><g fill="none" stroke="var(--green)" stroke-width="4"><path d="M8 22a11 11 0 0 1 19-13"/><path d="M30 16a11 11 0 0 1-19 13"/></g><path d="M23 4l8 1-1 8z M15 34l-8-1 1-8z" fill="var(--green)"/></svg>
    <span>Scan</span>
  </div>
  <div class="tab">
    <svg viewBox="0 0 46 46"><g fill="var(--green)"><path d="M14 4l-8 20h7l-4 18 14-24h-8l6-14z"/><path d="M30 4l-8 20h7l-4 18 14-24h-8l6-14z"/></g></svg>
    <span>Optimization</span>
  </div>
  <div class="tab" style="background:linear-gradient(#333,#151515)">
    <svg viewBox="0 0 46 46"><rect x="4" y="15" width="34" height="16" rx="2" fill="none" stroke="var(--green)" stroke-width="3"/><rect x="39" y="20" width="4" height="6" fill="var(--green)"/></svg>
    <span>Battery Status</span>
  </div>
  <div class="tab">
    <svg viewBox="0 0 46 46"><path d="M23 3l5 6 8-2 1 8 7 4-4 7 4 7-7 4-1 8-8-2-5 6-5-6-8 2-1-8-7-4 4-7-4-7 7-4 1-8 8 2z" fill="var(--green)"/><circle cx="23" cy="23" r="6" fill="#1a1a1a"/></svg>
    <span>Special Offer</span>
  </div>
  <div class="tab">
    <svg viewBox="0 0 40 40"><path d="M17 3h6l1 5 4 2 4-3 4 4-3 4 2 4 5 1v6l-5 1-2 4 3 4-4 4-4-3-4 2-1 5h-6l-1-5-4-2-4 3-4-4 3-4-2-4-5-1v-6l5-1 2-4-3-4 4-4 4 3 4-2z" fill="var(--green)"/><circle cx="20" cy="20" r="6" fill="#1a1a1a"/></svg>
    <span>Setting</span>
  </div>
</nav>

</body>
</html>
```